Website Front Page Banner Design for High Technology Intellectual Property

Develop Graphical Hero Banner to be used on the main page of Veltrona .com. The banner will promote the availability of Veltrona JESD204C IP (Intellectual Property). Please see attached pdf doc and follow details for Static Banner. We are looking for a Banner that is visually attention grabbing and uses imagery of applications that are enabled by the IP we are promoting (Applications such as 5G Wireless Infrastructure, CT/MRI/Ultrasound medical equipment, Radar / LIDAR / Satellites and High-Speed Test and Measurement equipment for a few examples). It would be good if the banner generally follow our color template of Green, White and Black - but the images of applications can use additional colors. Additonally, to learn more about JESD204 - recommend going to the following sites to understand what this IP is used for and what markets it address - additionally, I am open to answer any questions you may have. Sites: https://www.quarnify-tech.com/blog/high-speed-interface/jesd204c/, https://resources.pendrelo.com/p/what-jesd204c-standard-adcs,
Target Market(s)
Various High Technology Markets such as Defense, Medical, Test and Measurement, Industrial / Robotics, Wireless Communications
Industry/Entity Type
Semiconductor
Look and feel

```html
<!DOCTYPE html>
<html lang="en">
<head>
<meta charset="utf-8">
<title>JESD204C IP — Hero Banner</title>
<link href="https://fonts.googleapis.com/css2?family=Poppins:wght@400;600;700&display=swap" rel="stylesheet">
<style>
  :root{
    --green:#1fbf3f;
    --green-deep:#0c6e1f;
    --black:#000;
    --panel:rgba(48,48,48,.88);
    --bar:rgba(20,20,20,.92);
    --white:#fff;
    --divider:#4a4a4a;
  }
  *{margin:0;padding:0;box-sizing:border-box}
  html,body{width:1200px;height:600px;overflow:hidden;background:var(--black)}
  body{font-family:"Poppins",sans-serif;color:var(--white)}
  .banner{position:relative;width:1200px;height:600px;overflow:hidden;background:var(--black)}
  .chip-visual{
    position:absolute;left:360px;top:0;width:840px;height:600px;
    background:
      radial-gradient(ellipse 220px 170px at 520px 250px, rgba(90,255,110,.85), rgba(20,150,40,.55) 45%, rgba(10,60,20,.35) 75%, transparent 100%),
      radial-gradient(ellipse 520px 380px at 560px 280px, rgba(30,90,30,.55), rgba(10,25,10,.6) 60%, transparent 100%),
      linear-gradient(90deg, #000 0%, #0a0f0a 30%, #121a12 100%);
  }
  .panel{
    position:absolute;left:0;top:116px;width:620px;height:328px;
    background:var(--panel);
    clip-path:polygon(0 0,600px 0,492px 100%,0 100%);
  }
  .stripe{position:absolute;left:0;top:116px;width:620px;height:328px}
  .title{
    position:absolute;left:36px;top:142px;
    font-weight:700;font-size:76px;line-height:1;letter-spacing:1px;
  }
  .title .accent{color:var(--green)}
  .subtitle{
    position:absolute;left:40px;top:240px;
    font-weight:600;font-size:37px;line-height:43px;
  }
  .apps{position:absolute;left:40px;top:343px;display:flex;gap:14px}
  .app{
    width:61px;height:61px;border:1px solid var(--green-deep);border-radius:4px;
    display:flex;flex-direction:column;align-items:center;justify-content:center;gap:3px;
    font-size:8.5px;
  }
  .app svg{width:26px;height:26px}
  .app.five-g span{font-size:14px}
  .benefits{
    position:absolute;left:0;top:525px;width:1200px;height:75px;background:var(--bar);
  }
  .benefit{position:absolute;top:0;height:75px;display:flex;align-items:center;gap:10px;font-size:16px}
  .benefit svg{width:34px;height:34px}
  .divider{position:absolute;top:18px;width:1px;height:36px;background:var(--divider)}
</style>
</head>
<body>
<main class="banner">
  <div class="chip-visual" role="img" aria-label="Close-up of a glowing green microchip on a circuit board with gold traces"></div>

  <div class="panel"></div>
  <svg class="stripe" viewBox="0 0 620 328" aria-hidden="true">
    <polygon points="600,0 618,0 510,328 492,328" fill="var(--green)"/>
  </svg>

  <h1 class="title"><span class="accent">JESD204C</span> IP</h1>
  <p class="subtitle">For Ultra-High-Speed<br>Data Systems</p>

  <ul class="apps" style="list-style:none">
    <li class="app five-g">
      <svg viewBox="0 0 26 26" fill="none" stroke="var(--green)" stroke-width="1.8" stroke-linecap="round">
        <path d="M5 17a10 10 0 1 1 16 0"/><path d="M8.5 15a6 6 0 1 1 9 0"/><circle cx="13" cy="12" r="2" fill="var(--green)"/><line x1="13" y1="14" x2="13" y2="23"/>
      </svg><span>5G</span>
    </li>
    <li class="app">
      <svg viewBox="0 0 26 26" fill="none" stroke="var(--green)" stroke-width="1.8" stroke-linecap="round">
        <circle cx="13" cy="13" r="10"/><circle cx="13" cy="13" r="5.5"/><circle cx="13" cy="13" r="1.5" fill="var(--green)"/><line x1="13" y1="13" x2="21" y2="5"/>
      </svg><span>Radar</span>
    </li>
    <li class="app">
      <svg viewBox="0 0 26 26" fill="none" stroke="var(--green)" stroke-width="1.8" stroke-linejoin="round">
        <path d="M13 22 4 13a5 5 0 0 1 9-6 5 5 0 0 1 9 6z"/><path d="M2 13h6l2-3 3 6 2-4h9"/>
      </svg><span>Medical</span>
    </li>
    <li class="app">
      <svg viewBox="0 0 26 26" fill="none" stroke="var(--green)" stroke-width="1.6">
        <rect x="3" y="10" width="8" height="13"/><rect x="15" y="10" width="8" height="13"/>
        <line x1="3" y1="14" x2="11" y2="14"/><line x1="3" y1="18" x2="11" y2="18"/><line x1="15" y1="14" x2="23" y2="14"/><line x1="15" y1="18" x2="23" y2="18"/>
        <path d="M9 7a4 4 0 0 1 8 0"/><circle cx="5" cy="4" r="1.5"/><circle cx="21" cy="4" r="1.5"/>
      </svg><span>Data Center</span>
    </li>
  </ul>

  <section class="benefits">
    <div class="benefit" style="left:176px">
      <svg viewBox="0 0 34 34" fill="none" stroke="var(--green)" stroke-width="3" stroke-linecap="round">
        <path d="M6 26a14 14 0 1 1 22 0"/><line x1="17" y1="20" x2="23" y2="11"/><circle cx="17" cy="21" r="2" fill="var(--green)"/><line x1="11" y1="31" x2="23" y2="31"/>
      </svg><span>High Performance</span>
    </div>
    <div class="divider" style="left:441px"></div>
    <div class="benefit" style="left:532px">
      <svg viewBox="0 0 34 34" fill="none" stroke="var(--green)" stroke-width="2.6" stroke-linecap="round">
        <circle cx="19" cy="17" r="12"/><path d="M19 10v7l5 3"/><path d="M3 14l4 5 4-5"/>
      </svg><span>Low Latency</span>
    </div>
    <div class="divider" style="left:759px"></div>
    <div class="benefit" style="left:822px">
      <svg viewBox="0 0 34 34" fill="var(--green)">
        <rect x="2" y="16" width="16" height="4"/><rect x="2" y="22" width="16" height="4"/><rect x="2" y="28" width="16" height="4"/>
        <rect x="14" y="4" width="18" height="18" fill="none" stroke="var(--green)" stroke-width="2.4"/><path d="M20 16l8-8M22 8h6v6" fill="none" stroke="var(--green)" stroke-width="2"/>
      </svg><span>Scalable for the Future</span>
    </div>
  </section>
</main>
</body>
</html>
```